Fabrication and machining company needing printed material designs.

Heronfield Vessels, Inc. wants to use appealing visuals as well as informative text to tell potential clients about our capabilities in fabrication and machining. We have a new logo to showcase as well as a new website. The use of print media will allow us to leave tangible information with clients, and therefore the design will need to be concise, informative, and visually appealing.

Full Page Flyer (approx. 8.5" x 11"), front and back design. This will be a detailed offering of capabilities and services for our shop.

Half Page Flyer (approx. 5.5" x 8.5"), front and back design. An abbreviated version of the full page flyer, meant to be easily handed out and stored inside a note book.

Bi-fold business card front and back. General offerings of our services. Minimal if any details. Finished size is twice the size of a business card (approx. 4" x 3.5"), once folded in half will be the same size as a standard business card (approx. 2" x 3.5").

Please use www.heronfieldvesselsinc.example for theme ideas. The font used for our logo is ethnocentric, not to be used for all text.

Target Market(s)

Industrial Consumers

Font styles to use
Sans Serif

```html
<!DOCTYPE html>
<html lang="en">
<head>
<meta charset="utf-8">
<title>Heronfield Vessels – Flyer Front and Back</title>
<link href="https://fonts.googleapis.com/css2?family=Lato:ital,wght@0,400;0,700;0,900;1,700;1,900&family=Michroma&display=swap" rel="stylesheet">
<style>
:root{
  --bg:#262627;
  --slate:#3e3e41;
  --slate-light:#58585c;
  --blue:#5b8fd2;
  --blue-deep:#3f74bd;
  --orange:#f07d22;
  --white:#ffffff;
  --ink-soft:#d9dbe0;
}
*{margin:0;padding:0;box-sizing:border-box}
html,body{width:1200px;height:776px;overflow:hidden;background:var(--bg)}
body{position:relative;font-family:'Lato',sans-serif;color:var(--white)}
.flyer{position:absolute;top:48px;width:520px;height:680px;background:var(--white);overflow:hidden;box-shadow:0 10px 30px rgba(0,0,0,.45)}
.flyer--front{left:50px}
.flyer--back{left:630px;background:var(--slate)}
.abs{position:absolute}
.brand-mark{display:flex;align-items:center;gap:8px;font-weight:900;color:var(--white);font-size:14px;letter-spacing:1px;line-height:1.1}
.brand-mark__dot{width:14px;height:14px;background:var(--white);flex:none}
.brand-mark--front{left:26px;top:32px}
.brand-mark--back{left:22px;top:36px;font-size:12px}
.orange-rule{height:3px;background:var(--orange)}
.photo{border:4px solid var(--white)}
.heading-display{font-family:'Michroma',sans-serif;text-transform:uppercase}

/* front */
.front-header{left:0;top:0;width:520px;height:95px}
.front-wordmark{right:26px;top:22px;font-weight:900;font-size:27px;color:var(--blue);line-height:1;text-align:right;letter-spacing:1px}
.hero{left:0;top:95px;width:520px;height:245px;background:var(--blue)}
.hero__photo{left:150px;top:0;width:370px;height:245px;
  background:linear-gradient(90deg,var(--blue) 0%,rgba(91,143,210,0) 35%),
             linear-gradient(180deg,#4f86cf 0%,#8fb2de 30%,#a9a9a6 48%,#9b9c9e 64%,#c7cbd1 78%,#e2e5ea 100%)}
.hero__title{left:26px;top:56px;font-weight:900;font-size:31px;line-height:1.02;letter-spacing:1px;text-shadow:0 2px 4px rgba(0,0,0,.35)}
.hero__rule{left:26px;top:131px;width:230px}
.hero__tag{left:26px;top:140px;font-style:italic;font-weight:900;font-size:29px;line-height:1.1;text-shadow:0 2px 4px rgba(0,0,0,.35)}
.cards{left:14px;top:348px;width:492px;height:226px;background:var(--slate);display:flex}
.card{flex:1;padding:10px 9px;text-align:center}
.card:nth-child(2){background:var(--slate-light)}
.card .photo{height:98px}
.photo--shop{background:linear-gradient(180deg,#8a8378 0%,#b5ada0 40%,#4f6f9a 65%,#c8c6c2 100%)}
.photo--crane{background:linear-gradient(180deg,#6c9bd8 0%,#a9c5e8 45%,#d9cfb8 62%,#8a7d68 85%,#c9b79a 100%)}
.photo--truck{background:linear-gradient(180deg,#7aa6e0 0%,#a8c3e6 40%,#4a4d52 60%,#3a3c40 80%,#b7ad98 100%)}
.card__title{margin:9px auto 5px;font-weight:700;font-size:13px;text-transform:uppercase;display:inline-block;padding-bottom:3px;border-bottom:2px solid var(--orange)}
.card__text{font-size:9px;line-height:1.35;color:var(--ink-soft)}
.front-footer{left:0;top:585px;width:520px;height:95px;background:var(--blue)}
.contact-row{position:absolute;left:0;right:0;display:flex;justify-content:center;align-items:flex-end;gap:10px;font-size:12px}
.contact-item{display:flex;flex-direction:column;align-items:center;gap:6px}
.contact-sep{width:2px;height:18px;background:currentColor;opacity:.8}

/* back */
.back-header{left:0;top:0;width:520px;height:100px}
.back-header__photo{left:318px;top:10px;width:190px;height:88px;background:linear-gradient(180deg,#3f7fd6 0%,#8db6ea 45%,#c9d8ec 68%,#6f6a5f 82%,#8c8474 100%)}
.about{left:0;top:100px;width:520px;height:72px;background:var(--blue);padding:10px 22px}
.about__title{font-size:19px;letter-spacing:1px}
.about__text{font-size:6.5px;line-height:1.35;margin-top:5px;color:#eef3fb}
.industries__title{left:0;width:520px;top:200px;text-align:center;font-size:20px;letter-spacing:1px}
.industries__rule{left:185px;top:232px;width:150px}
.industries__photo{left:182px;top:262px;width:156px;height:80px;border-radius:2px;
  background:linear-gradient(180deg,rgba(62,62,65,0) 0%,#d2cfc2 20%,#bcb8aa 55%,#8f8a7e 75%,#6e6a61 88%,rgba(62,62,65,0) 100%)}
.industries__name{left:0;width:520px;top:356px;text-align:center;font-weight:900;font-size:17px;letter-spacing:1px}
.industry-label{font-size:10px;text-align:center;line-height:1.15}
.offer{left:0;top:530px;width:520px;height:68px;background:var(--white);display:flex;align-items:center;padding:0 24px;gap:14px}
.offer__title{color:var(--blue-deep);font-size:19px;line-height:1.1;text-align:right;text-transform:uppercase;font-weight:400;padding-right:14px;border-right:2px solid var(--blue-deep)}
.offer__list{list-style:none;color:var(--blue-deep);font-size:10px;line-height:1.45;text-transform:uppercase}
.back-footer{left:0;top:598px;width:520px;height:82px;color:var(--blue)}
</style>
</head>
<body>

<section class="flyer flyer--front">
  <svg class="abs front-header" width="520" height="95" viewBox="0 0 520 95" aria-hidden="true">
    <polygon points="0,0 275,0 235,95 0,95" fill="#3e3e41"/>
  </svg>
  <div class="abs brand-mark brand-mark--front"><span class="brand-mark__dot"></span><span>HERONFIELD<br>VESSELS INC.</span></div>
  <div class="abs front-wordmark">HERONFIELD<br>VESSELS INC.</div>

  <div class="abs hero">
    <div class="abs hero__photo" role="img" aria-label="Photo of large grey storage tanks at an industrial site under a blue sky"></div>
    <div class="abs hero__title">HERONFIELD<br>VESSELS INC.</div>
    <div class="abs orange-rule hero__rule"></div>
    <div class="abs hero__tag">is a leading tank<br>manufacturer.</div>
  </div>

  <div class="abs cards">
    <article class="card">
      <div class="photo photo--shop" role="img" aria-label="Photo of pump equipment inside the fabrication shop"></div>
      <h3 class="card__title">Who we are</h3>
      <p class="card__text">Our world runs on natural and renewable resources. We are proud to make our livelihood supporting the industries that provide our quality of life.</p>
    </article>
    <article class="card">
      <div class="photo photo--crane" role="img" aria-label="Photo of a crane lifting a tank beside finished tanks"></div>
      <h3 class="card__title">Why choose us</h3>
      <p class="card__text">It all begins with integrity. We pride ourselves in the craftsmanship we send our customers. From concept through delivery we strive for excellence.</p>
    </article>
    <article class="card">
      <div class="photo photo--truck" role="img" aria-label="Photo of a dark tank loaded on a transport truck"></div>
      <h3 class="card__title">Our team</h3>
      <p class="card__text">We are welders and fabricators, as well as parents, neighbors, and civic volunteers. We take our work ethic and use it to build a better community.</p>
    </article>
  </div>

  <div class="abs front-footer">
    <div class="contact-row" style="top:22px">
      <div class="contact-item">
        <svg width="26" height="26" viewBox="0 0 26 26" aria-hidden="true"><circle cx="13" cy="13" r="12" fill="none" stroke="#fff" stroke-width="1.3"/><path d="M13 6a4.5 4.5 0 0 0-4.5 4.5c0 3.5 4.5 8.5 4.5 8.5s4.5-5 4.5-8.5A4.5 4.5 0 0 0 13 6z" fill="none" stroke="#fff" stroke-width="1.3"/><circle cx="13" cy="10.5" r="1.6" fill="#fff"/></svg>
        <span>PO Box 412 Alderton UT 84990</span>
      </div>
      <span class="contact-sep"></span>
      <div class="contact-item">
        <svg width="26" height="26" viewBox="0 0 26 26" aria-hidden="true"><circle cx="13" cy="13" r="12" fill="none" stroke="#fff" stroke-width="1.3"/><rect x="7" y="9" width="12" height="8.5" fill="none" stroke="#fff" stroke-width="1.3"/><path d="M7 9l6 5 6-5" fill="none" stroke="#fff" stroke-width="1.3"/></svg>
        <span>office@heronfieldvesselsinc.example</span>
      </div>
      <span class="contact-sep"></span>
      <div class="contact-item">
        <svg width="26" height="26" viewBox="0 0 26 26" aria-hidden="true"><circle cx="13" cy="13" r="12" fill="none" stroke="#fff" stroke-width="1.3"/><path d="M9 7.5l2.3 2.6-1.2 1.6a8 8 0 0 0 4.2 4.2l1.6-1.2 2.6 2.3-1.4 1.7C12 18.5 7.5 14 7.3 8.9z" fill="none" stroke="#fff" stroke-width="1.3"/></svg>
        <span>(555) 014-2698</span>
      </div>
    </div>
  </div>
</section>

<section class="flyer flyer--back">
  <svg class="abs back-header" width="520" height="100" viewBox="0 0 520 100" aria-hidden="true">
    <rect width="520" height="100" fill="#ffffff"/>
    <polygon points="0,0 250,0 215,100 0,100" fill="#3e3e41"/>
    <polygon points="215,100 250,0 290,0 255,100" fill="#5b8fd2"/>
  </svg>
  <div class="abs brand-mark brand-mark--back"><span class="brand-mark__dot"></span><span>HERONFIELD<br>VESSELS INC.</span></div>
  <div class="abs photo back-header__photo" role="img" aria-label="Photo of a large national flag hung from crane booms over a yard"></div>

  <div class="abs about">
    <h2 class="heading-display about__title">About us</h2>
    <p class="about__text">Heronfield Vessels Inc. is a leading tank manufacturer serving the mountain west. We specialize in API-12F and API-650 tanks and custom fabrication for energy, water and mining customers. Our shop also builds cone bottom and mixer tanks, pump skids, and stairways, and now offers machining services and stainless steel work in a separate facility.</p>
  </div>

  <h2 class="abs heading-display industries__title">Industries served</h2>
  <div class="abs orange-rule industries__rule"></div>

  <svg class="abs" style="left:0;top:0" width="520" height="530" viewBox="0 0 520 530" aria-hidden="true">
    <path d="M108 282 Q120 470 260 478 Q410 470 420 255" fill="none" stroke="#ffffff" stroke-width="2.5" stroke-dasharray="0.1 9" stroke-linecap="round"/>
    <g fill="none" stroke="#ffffff" stroke-width="1.4">
      <circle cx="78" cy="268" r="20"/>
      <circle cx="82" cy="400" r="20"/>
      <circle cx="262" cy="405" r="20"/>
      <circle cx="462" cy="235" r="20"/>
      <circle cx="462" cy="368" r="20"/>
    </g>
    <g fill="none" stroke="#ffffff" stroke-width="1.6" stroke-linejoin="round" stroke-linecap="round">
      <path d="M78 257 C85 264 87 270 85 274 A7 7 0 0 1 71 274 C69 269 73 265 78 257z"/>
      <path d="M78 268 C81 271 81 274 78 276 C75 274 75 271 78 268z"/>
      <path d="M82 389 C88 397 90 401 90 404 A8 8 0 0 1 74 404 C74 401 76 397 82 389z"/>
      <path d="M72 414 H92"/>
      <path d="M253 396 L271 414 M271 396 L253 414"/>
      <path d="M249 399 Q253 392 258 391 M275 399 Q271 392 266 391"/>
      <path d="M465 223 L455 237 H462 L458 248 L470 232 H463z"/>
      <path d="M450 378 L462 360 L474 378z"/>
      <path d="M447 381 H477"/>
    </g>
    <g fill="#f07d22" stroke="#ffffff" stroke-width="2.5">
      <circle cx="112" cy="262" r="7"/>
      <circle cx="128" cy="400" r="7"/>
      <circle cx="262" cy="458" r="7"/>
      <circle cx="432" cy="235" r="7"/>
      <circle cx="432" cy="370" r="7"/>
    </g>
  </svg>
  <div class="abs industries__photo" role="img" aria-label="Photo of a row of production tanks on a steel base"></div>
  <div class="abs industries__name">HERONFIELD VESSELS</div>
  <div class="abs industry-label" style="left:56px;top:294px;width:44px">Oil &amp;<br>Gas</div>
  <div class="abs industry-label" style="left:40px;top:426px;width:90px">Water &amp; Waste<br>Water</div>
  <div class="abs industry-label" style="left:232px;top:470px;width:60px">MINING</div>
  <div class="abs industry-label" style="left:430px;top:258px;width:70px">Power<br>Generation</div>
  <div class="abs industry-label" style="left:430px;top:392px;width:70px">Aggregate</div>

  <div class="abs offer">
    <div class="offer__title">Oil production<br>tanks &amp; accessories</div>
    <ul class="offer__list">
      <li>• API 12-F, API 650 specification built tanks</li>
      <li>• Fire tubes/tank heaters</li>
      <li>• Tank coils • Walkways • Stairs</li>
    </ul>
  </div>

  <div class="abs back-footer">
    <div class="contact-row" style="top:18px">
      <div class="contact-item">
        <svg width="26" height="26" viewBox="0 0 26 26" aria-hidden="true"><circle cx="13" cy="13" r="12" fill="none" stroke="#5b8fd2" stroke-width="1.3"/><path d="M13 6a4.5 4.5 0 0 0-4.5 4.5c0 3.5 4.5 8.5 4.5 8.5s4.5-5 4.5-8.5A4.5 4.5 0 0 0 13 6z" fill="none" stroke="#5b8fd2" stroke-width="1.3"/><circle cx="13" cy="10.5" r="1.6" fill="#5b8fd2"/></svg>
        <span>PO Box 412 Alderton UT 84990</span>
      </div>
      <span class="contact-sep"></span>
      <div class="contact-item">
        <svg width="26" height="26" viewBox="0 0 26 26" aria-hidden="true"><circle cx="13" cy="13" r="12" fill="none" stroke="#5b8fd2" stroke-width="1.3"/><rect x="7" y="9" width="12" height="8.5" fill="none" stroke="#5b8fd2" stroke-width="1.3"/><path d="M7 9l6 5 6-5" fill="none" stroke="#5b8fd2" stroke-width="1.3"/></svg>
        <span>office@heronfieldvesselsinc.example</span>
      </div>
      <span class="contact-sep"></span>
      <div class="contact-item">
        <svg width="26" height="26" viewBox="0 0 26 26" aria-hidden="true"><circle cx="13" cy="13" r="12" fill="none" stroke="#5b8fd2" stroke-width="1.3"/><path d="M9 7.5l2.3 2.6-1.2 1.6a8 8 0 0 0 4.2 4.2l1.6-1.2 2.6 2.3-1.4 1.7C12 18.5 7.5 14 7.3 8.9z" fill="none" stroke="#5b8fd2" stroke-width="1.3"/></svg>
        <span>(555) 014-2698</span>
      </div>
    </div>
  </div>
</section>

</body>
</html>
```